Create a business promotion flyer to leave in customer mailboxes. We are a bulk petroleum supplier, servicing any industry that requires diesel. Base in griffith NSW, servicing griffith area and surrounds.

Business Name - Terra Petro
Fuel@terrapetro-example.com.au
Marco - 0400 000 001 mtorrisi@terrapetro-example.com.au
Liam - 0400 000 002 lharcourt@terrapetro-example.com.au
Peter - 0400 000 003 pwinslow@terrapetro-example.com.au
Office 02 5550 0100

Bulk Fuel deliveries.
Oils & lubricants
Local Family owned business

```html
<!DOCTYPE html>
<html lang="en">
<head>
<meta charset="utf-8">
<title>Terra Petro – Bulk Fuel Supplier</title>
<link href="https://fonts.googleapis.com/css2?family=Poppins:wght@400;500;600;700&family=Roboto+Condensed:wght@400;700;800&display=swap" rel="stylesheet">
<style>
  :root{
    --red:#e32822;
    --dark:#272a2e;
    --ink:#222428;
    --white:#ffffff;
    --pale:#ececec;
    --grey:#6b6b6b;
  }
  *{margin:0;padding:0;box-sizing:border-box}
  html,body{width:848px;height:1200px;overflow:hidden;background:var(--white)}
  .flyer{position:relative;width:848px;height:1200px;overflow:hidden;font-family:"Poppins",sans-serif;color:var(--ink)}
  .cond{font-family:"Roboto Condensed",sans-serif}

  .hero-shapes{position:absolute;left:0;top:0}
  .location{position:absolute;right:38px;top:48px;text-align:right;color:var(--white)}
  .location__title{font-family:"Roboto Condensed",sans-serif;font-weight:800;font-size:33px;line-height:1;color:var(--red);letter-spacing:-.2px}
  .location__sub{font-size:13px;font-weight:400;margin-top:5px;letter-spacing:.2px}

  .brand{position:absolute;left:57px;top:110px;display:flex;align-items:center;gap:12px}
  .brand__dot{width:40px;height:40px;border-radius:50%;background:var(--red)}
  .brand__name{font-weight:600;font-size:46px;color:var(--red);line-height:1;letter-spacing:-.5px}

  .headline{position:absolute;left:55px;top:232px}
  .headline__pre{font-weight:600;font-size:25px;line-height:1}
  .headline__main{font-family:"Roboto Condensed",sans-serif;font-weight:800;font-size:76px;line-height:.98;margin-top:8px;letter-spacing:-1px}
  .headline__main .red{color:var(--red)}
  .headline__rule{position:absolute;left:55px;top:427px;width:114px;height:4px;background:var(--red)}
  .intro{position:absolute;left:55px;top:445px;font-size:20px;line-height:25px;font-weight:400}

  .services{position:absolute;left:0;top:565px;width:848px;height:224px;background:var(--dark)}
  .service{position:absolute;top:0;width:240px;text-align:center;color:var(--white)}
  .service__icon{position:absolute;left:50%;top:-8px;margin-left:-45px;width:90px;height:90px;border-radius:50%;background:var(--red);border:3px solid var(--white);display:flex;align-items:center;justify-content:center}
  .service__title{margin-top:86px;font-weight:600;font-size:18.5px;line-height:25px;letter-spacing:.3px}
  .service__rule{width:56px;height:2px;background:var(--red);margin:8px auto 9px}
  .service__text{font-size:14px;line-height:16px;font-weight:400}

  .values{position:absolute;left:0;top:789px;width:848px;height:174px}
  .values__icon{position:absolute;left:54px;top:57px}
  .values__heading{position:absolute;left:143px;top:27px;font-family:"Roboto Condensed",sans-serif;font-weight:800;font-size:37px;line-height:41px;letter-spacing:-.3px}
  .values__heading .red{color:var(--red)}
  .values__divider{position:absolute;left:406px;top:30px;width:1px;height:114px;background:var(--ink)}
  .values__list{position:absolute;left:444px;top:32px;list-style:none}
  .values__list li{display:flex;align-items:center;gap:11px;font-weight:500;font-size:18px;height:31.5px;letter-spacing:.2px}

  .contact{position:absolute;left:0;top:963px;width:848px;height:152px;background:var(--dark);color:var(--white)}
  .contact__title{position:absolute;left:56px;top:50px;font-family:"Roboto Condensed",sans-serif;font-weight:800;font-size:37px;line-height:1;color:var(--red)}
  .contact__tag{position:absolute;left:58px;top:91px;font-size:11px;font-weight:500;letter-spacing:.2px}
  .person{position:absolute;top:50px}
  .person__name{display:flex;align-items:center;gap:4px;font-family:"Roboto Condensed",sans-serif;font-weight:700;font-size:26px;line-height:1;color:var(--red)}
  .person__phone{font-family:"Roboto Condensed",sans-serif;font-weight:400;font-size:27px;margin-top:8px;line-height:1}

  .footer{position:absolute;left:0;top:1115px;width:848px;height:85px;background:var(--red);color:var(--white);display:flex;align-items:center;justify-content:center}
  .footer__slashes{position:absolute;top:31px;font-family:"Roboto Condensed",sans-serif;font-weight:700;font-size:24px;letter-spacing:3px;color:#a81611;font-style:italic}
  .footer__email{display:flex;align-items:center;gap:6px;font-family:"Roboto Condensed",sans-serif;font-weight:700;font-size:33px;letter-spacing:3.2px}
</style>
</head>
<body>
<div class="flyer">

  <svg class="hero-shapes" width="848" height="565" viewBox="0 0 848 565">
    <defs>
      <linearGradient id="photoTone" x1="0" y1="0" x2="0" y2="1">
        <stop offset="0" stop-color="#4f7fc4"/>
        <stop offset=".35" stop-color="#a9c2e2"/>
        <stop offset=".5" stop-color="#cfd3d8"/>
        <stop offset=".72" stop-color="#e9e9ea"/>
        <stop offset="1" stop-color="#c8c6c2"/>
      </linearGradient>
    </defs>
    <polygon points="445,0 482,0 440,125 422,125" fill="#e32822"/>
    <polygon points="482,0 848,0 848,125 440,125" fill="#272a2e"/>
    <polygon points="422,125 448,125 335,565 305,565" fill="#ececec"/>
    <polygon role="img" aria-label="Photo of white fuel tanker trucks parked in front of a depot shed under a blue sky" points="448,125 848,125 848,565 335,565" fill="url(#photoTone)"/>
  </svg>

  <div class="location">
    <div class="location__title">BASED IN GRIFFITH NSW</div>
    <div class="location__sub">SERVICING GRIFFITH AREA AND SURROUNDS</div>
  </div>

  <div class="brand">
    <span class="brand__dot"></span>
    <span class="brand__name">Terra Petro</span>
  </div>

  <div class="headline">
    <div class="headline__pre">YOUR LOCAL</div>
    <div class="headline__main"><span class="red">BULK FUEL</span><br>SUPPLIER</div>
  </div>
  <div class="headline__rule"></div>
  <p class="intro">Bulk petroleum supplier,<br>servicing any industry<br>that requires diesel.</p>

  <section class="services">
    <div class="service" style="left:53px">
      <div class="service__icon">
        <svg width="52" height="36" viewBox="0 0 52 36" fill="none" stroke="#fff" stroke-width="2.4" stroke-linejoin="round">
          <rect x="2" y="4" width="28" height="22" rx="2"/>
          <path d="M30 10h10l8 8v8H30z"/>
          <path d="M34 12h6v6h-6z"/>
          <circle cx="12" cy="29" r="4" fill="#e32822"/>
          <circle cx="40" cy="29" r="4" fill="#e32822"/>
          <path d="M16 10c-2 3-3 5-3 6a3 3 0 006 0c0-1-1-3-3-6z" fill="#fff" stroke="none"/>
        </svg>
      </div>
      <div class="service__title">BULK FUEL<br>DELIVERIES</div>
      <div class="service__rule"></div>
      <div class="service__text">Reliable bulk diesel<br>deliveries when and<br>where you need it.</div>
    </div>
    <div class="service" style="left:293px">
      <div class="service__icon">
        <svg width="56" height="30" viewBox="0 0 56 30" fill="none" stroke="#fff" stroke-width="2.4" stroke-linejoin="round" stroke-linecap="round">
          <path d="M2 8l10 4"/>
          <path d="M12 10h22l10-6 6 2-14 20H14z"/>
          <path d="M20 6h10"/>
          <path d="M51 16c-1.5 2.5-2.5 4-2.5 5a2.5 2.5 0 005 0c0-1-1-2.5-2.5-5z" fill="#fff" stroke="none"/>
        </svg>
      </div>
      <div class="service__title">OILS &amp;<br>LUBRICANTS</div>
      <div class="service__rule"></div>
      <div class="service__text">Quality oils and<br>lubricants to keep your<br>equipment running</div>
    </div>
    <div class="service" style="left:535px">
      <div class="service__icon">
        <svg width="36" height="44" viewBox="0 0 36 44" fill="none" stroke="#fff" stroke-width="2.6" stroke-linejoin="round">
          <path d="M12 4h20v38H4V14z"/>
          <path d="M4 10l8-8"/>
          <path d="M18 18c-4 5-6 8-6 11a6 6 0 0012 0c0-3-2-6-6-11z" fill="#fff" stroke="none"/>
        </svg>
      </div>
      <div class="service__title">PETROL<br>DELIVERIES</div>
      <div class="service__rule"></div>
      <div class="service__text">Petrol deliveries<br>for equipment,<br>vehicles and more.</div>
    </div>
  </section>

  <section class="values">
    <svg class="values__icon" width="74" height="74" viewBox="0 0 74 74" fill="none" stroke-linejoin="round">
      <circle cx="37" cy="37" r="35.5" stroke="#222428" stroke-width="2.2"/>
      <path d="M14 36l23-19 23 19" stroke="#e32822" stroke-width="2.4"/>
      <path d="M19 32v22" stroke="#e32822" stroke-width="2.4"/>
      <g stroke="#e32822" stroke-width="2.2">
        <rect x="22" y="46" width="6" height="9"/>
        <rect x="31" y="40" width="6" height="15"/>
        <rect x="40" y="34" width="6" height="21"/>
        <rect x="49" y="38" width="6" height="17"/>
      </g>
    </svg>
    <h2 class="values__heading">LOCAL<br><span class="red">FAMILY OWNED</span><br>BUSINESS</h2>
    <div class="values__divider"></div>
    <ul class="values__list">
      <li><svg width="15" height="15" viewBox="0 0 15 15"><circle cx="7.5" cy="7.5" r="7.5" fill="#e32822"/><path d="M4 7.7l2.4 2.3L11 5.3" stroke="#fff" stroke-width="1.8" fill="none"/></svg>LOCAL PEOPLE, LOCAL SERVICE</li>
      <li><svg width="15" height="15" viewBox="0 0 15 15"><circle cx="7.5" cy="7.5" r="7.5" fill="#e32822"/><path d="M4 7.7l2.4 2.3L11 5.3" stroke="#fff" stroke-width="1.8" fill="none"/></svg>RELIABLE &amp; ON TIME</li>
      <li><svg width="15" height="15" viewBox="0 0 15 15"><circle cx="7.5" cy="7.5" r="7.5" fill="#e32822"/><path d="M4 7.7l2.4 2.3L11 5.3" stroke="#fff" stroke-width="1.8" fill="none"/></svg>COMPETITIVE PRICING</li>
      <li><svg width="15" height="15" viewBox="0 0 15 15"><circle cx="7.5" cy="7.5" r="7.5" fill="#e32822"/><path d="M4 7.7l2.4 2.3L11 5.3" stroke="#fff" stroke-width="1.8" fill="none"/></svg>SUPPORTING LOCAL INDUSTRY</li>
    </ul>
  </section>

  <section class="contact">
    <h2 class="contact__title">GET IN TOUCH</h2>
    <p class="contact__tag">WE'RE LOCAL, RELIABLE AND READY TO HELP.</p>
    <div class="person" style="left:341px">
      <div class="person__name"><svg width="15" height="15" viewBox="0 0 15 15"><circle cx="7.5" cy="7.5" r="7.5" fill="#e32822"/><path d="M5 4.2l1.4-.4.9 2-1 .8a5 5 0 002.2 2.2l.8-1 2 .9-.4 1.4c-3.5.3-6.2-2.4-5.9-5.9z" fill="#fff"/></svg>MARCO</div>
      <div class="person__phone">0400 000 001</div>
    </div>
    <div class="person" style="left:504px">
      <div class="person__name"><svg width="15" height="15" viewBox="0 0 15 15"><circle cx="7.5" cy="7.5" r="7.5" fill="#e32822"/><path d="M5 4.2l1.4-.4.9 2-1 .8a5 5 0 002.2 2.2l.8-1 2 .9-.4 1.4c-3.5.3-6.2-2.4-5.9-5.9z" fill="#fff"/></svg>LIAM</div>
      <div class="person__phone">0400 000 002</div>
    </div>
    <div class="person" style="left:662px">
      <div class="person__name"><svg width="15" height="15" viewBox="0 0 15 15"><circle cx="7.5" cy="7.5" r="7.5" fill="#e32822"/><path d="M5 4.2l1.4-.4.9 2-1 .8a5 5 0 002.2 2.2l.8-1 2 .9-.4 1.4c-3.5.3-6.2-2.4-5.9-5.9z" fill="#fff"/></svg>PETER</div>
      <div class="person__phone">0400 000 003</div>
    </div>
  </section>

  <footer class="footer">
    <span class="footer__slashes" style="left:62px">//////</span>
    <div class="footer__email">
      <svg width="28" height="28" viewBox="0 0 28 28" fill="none" stroke="#fff" stroke-width="2"><circle cx="14" cy="14" r="12"/><ellipse cx="14" cy="14" rx="5" ry="12"/><path d="M2 14h24M4 8h20M4 20h20"/></svg>
      Fuel@terrapetro-example.com.au
    </div>
    <span class="footer__slashes" style="right:62px">//////</span>
  </footer>

</div>
</body>
</html>
```